Minimalist, Flat(Matte) design for a Beef Jerky packaging company. No bullshit company looking for a

Need a packaging design for a new Beef Jerky product(in English). The name of the company is 'Velmor' and thus the packaging should reflect the bullish, tough, and simple nature of the beef jerky product. The finished product should communicate simplicity, minimalism, yet toughness and strength.

The logo should be simple, with a minimal number of colors , and should be either all white/cream, or have some red as well. Main colors should be white, cream, tinted red, and matte black. I think 4 colors max would be best. The closest example to an existing package style would be Korvanti Dusk clove cigarettes( image attached).

It will be on a matte black standing pouch package. See image for package type. Package dimensions:

Dimension: Width x Gusset x Height
INCH : 5.125" (W) x 3.125" (G) x 8.125" (H)
MILLIMETER : 130mm (W) x 80mm (G) x 205mm (H)

I don't have anything totally specific so artistic liberty is encouraged, provided the colors are kept to a minimum and looks consistent with the simple nature of the brand and the matte black packaging.

Also attached an existing beef jerky package with a similar style to what we're looking for.

Industry/Entity Type

It Company

Colors
f59195
ffffff

Requirements
Must have
• Low contrast, flat and minimalist design.
Should not have
• A complicated design with many colors. Gawdy/flashy design. Bright colors. High contrast.

```html
<!DOCTYPE html>
<html lang="en">
<head>
<meta charset="utf-8">
<title>Velmor Peppered Beef Jerky – Pouch Front</title>
<link rel="stylesheet" href="https://fonts.googleapis.com/css2?family=Roboto+Condensed:wght@400;700&family=Pinyon+Script&display=swap">
<style>
  :root {
    --backdrop: #ececec;
    --pouch-black: #141414;
    --pouch-glow: #4a4a4a;
    --ink-white: #ffffff;
    --accent-red: #d5393d;
  }
  * { margin: 0; padding: 0; box-sizing: border-box; }
  html, body {
    width: 1200px;
    height: 1195px;
    overflow: hidden;
    background: var(--backdrop);
  }
  .canvas {
    position: relative;
    width: 1200px;
    height: 1195px;
  }
  .pouch-front {
    position: absolute;
    left: 282px;
    top: 185px;
    width: 623px;
    height: 850px;
    border-radius: 14px;
    background: radial-gradient(ellipse 260px 300px at 50% 42%, var(--pouch-glow), var(--pouch-black) 100%);
    color: var(--ink-white);
    font-family: "Roboto Condensed", sans-serif;
  }
  .line-text {
    position: absolute;
    left: 0;
    width: 100%;
    text-align: center;
    white-space: nowrap;
  }
  .tagline {
    top: 152px;
    font-size: 20px;
    font-weight: 700;
    letter-spacing: 4px;
  }
  .brand-name {
    top: 385px;
    font-size: 112px;
    font-weight: 400;
    letter-spacing: 4px;
    line-height: 1;
  }
  .flavour {
    top: 548px;
    font-family: "Pinyon Script", cursive;
    font-size: 42px;
    line-height: 1;
  }
  .divider {
    position: absolute;
    left: 148px;
    top: 608px;
    width: 375px;
    height: 3px;
    background: var(--ink-white);
  }
  .product-name {
    top: 620px;
    font-size: 60px;
    font-weight: 700;
    line-height: 1;
  }
  .grade {
    top: 747px;
    font-size: 20px;
    font-weight: 700;
    letter-spacing: 16px;
    padding-left: 16px;
  }
  .net-weight {
    top: 776px;
    font-size: 16px;
    font-weight: 700;
  }
</style>
</head>
<body>
  <main class="canvas">
    <section class="pouch-front" aria-label="Velmor peppered beef jerky pouch front">
      <p class="line-text tagline">HAND CRAFTED</p>
      <h1 class="line-text brand-name">VELMOR</h1>
      <p class="line-text flavour">Peppered</p>
      <div class="divider"></div>
      <h2 class="line-text product-name">BEEF JERKY</h2>
      <p class="line-text grade">PREMIUM</p>
      <p class="line-text net-weight">NET WT. 3 OZ</p>
    </section>
  </main>
</body>
</html>
```